Lantern Advisory Website

I currently have a website www.lanternadvisoryinc.example. We are a IT Consulting Company. Our website will pretty much tell out our services. I am looking to enhance my website and make it look more professional. Looking for very classy and Contemporary look and design for my website.

It Company

```html
<!DOCTYPE html>
<html lang="en">
<head>
<meta charset="utf-8">
<title>Lantern Advisory</title>
<link href="https://fonts.googleapis.com/css2?family=Open+Sans:wght@400;600;700&display=swap" rel="stylesheet">
<style>
:root{
  --blue:#1d87d4;
  --blue-dark:#0d5fa6;
  --navy:#0a4d8c;
  --sky:#3fa6e6;
  --pale:#f3f5f7;
  --text:#5b6470;
  --white:#ffffff;
  --line:#e3e7eb;
}
*{box-sizing:border-box;margin:0;padding:0}
html,body{width:1200px;height:2568px;overflow:hidden}
body{font-family:"Open Sans",Arial,sans-serif;color:var(--text);background:var(--white);position:relative}
.site-header{position:absolute;top:0;left:0;width:1200px;height:88px;background:var(--white)}
.brand{position:absolute;left:120px;top:22px;display:flex;align-items:center;gap:10px}
.brand-mark{width:40px;height:40px;background:var(--blue)}
.brand-name{font-size:20px;font-weight:700;color:var(--blue-dark);line-height:1}
.header-swoosh{position:absolute;left:330px;top:0}
.main-nav{position:absolute;right:110px;top:0;height:72px;display:flex;align-items:center;gap:34px}
.main-nav a{font-size:14px;font-weight:700;color:var(--white);text-decoration:none;letter-spacing:.5px}
.hero{position:absolute;top:88px;left:0;width:1200px;height:512px;overflow:hidden}
.hero-photo{position:absolute;inset:0;background:radial-gradient(circle at 62% 40%,#7cc3f0 0%,#2d8fd6 35%,#0f5fae 75%,#0a4a8f 100%)}
.hero-content{position:absolute;left:130px;top:210px;width:470px;color:var(--white)}
.hero-title{font-size:34px;font-weight:700;letter-spacing:1px;margin-bottom:18px}
.hero-text{font-size:14px;line-height:1.6;margin-bottom:26px}
.btn{display:inline-block;background:var(--navy);color:var(--white);font-size:12px;font-weight:700;padding:12px 22px;letter-spacing:.5px}
.btn-outline{background:var(--white);color:var(--blue);border:1px solid var(--blue)}
.dots{position:absolute;display:flex;gap:8px;left:50%;transform:translateX(-50%)}
.dots span{width:10px;height:10px;border-radius:50%;background:rgba(255,255,255,.5)}
.dots span.on{background:var(--white)}
.welcome{position:absolute;top:600px;left:0;width:1200px;height:340px;text-align:center}
.section-title{font-size:24px;font-weight:700;color:var(--blue);text-transform:uppercase;letter-spacing:.5px}
.welcome .section-title{margin-top:56px}
.welcome p{width:820px;margin:30px auto 34px;font-size:14px;line-height:1.75}
.services{position:absolute;top:940px;left:0;width:1200px;height:420px;background:var(--pale);text-align:center}
.services .section-title{margin-top:60px}
.service-row{display:flex;gap:56px;justify-content:center;margin-top:56px}
.service-card{width:296px;text-align:left}
.service-head{display:flex;align-items:center;gap:12px;padding-bottom:16px;border-bottom:2px solid var(--line)}
.service-icon{width:40px;height:40px;border-radius:50%;border:2px solid var(--blue);display:flex;align-items:center;justify-content:center}
.service-name{font-size:17px;font-weight:700;color:var(--blue-dark);text-transform:uppercase}
.service-card p{font-size:12px;line-height:1.7;margin-top:16px}
.services .dots{top:356px}
.services .dots span{background:#c6ccd2}
.services .dots span.on{background:var(--blue)}
.feature{position:absolute;left:0;width:1200px;height:360px}
.feature-photo{position:absolute;width:290px;height:290px;border-radius:50%;border:8px solid var(--white);top:35px}
.feature-body{position:absolute;top:70px}
.feature-title{font-size:22px;font-weight:700;text-transform:uppercase;margin-bottom:22px}
.feature-body p{font-size:13px;line-height:1.75;margin-bottom:18px}
.it{top:1360px;background:var(--navy);color:var(--white)}
.it .feature-photo{left:150px;background:linear-gradient(135deg,#e8eef3,#a9bccc 55%,#6f8aa3)}
.it .feature-body{left:520px;width:560px}
.staff{top:1720px;background:var(--white)}
.staff .feature-photo{left:760px;background:linear-gradient(160deg,#dfeaf5,#8fb3d6 50%,#3c6f9f);border-color:#e9eef2}
.staff .feature-body{left:140px;width:540px;top:80px}
.staff .feature-title{color:var(--blue)}
.offshore{top:2080px;background:var(--sky);color:var(--white)}
.offshore .feature-photo{left:150px;background:linear-gradient(135deg,#f2f2f2,#bfc5ca 55%,#7d868e)}
.offshore .feature-body{left:520px;width:560px;top:100px}
.site-footer{position:absolute;top:2440px;left:0;width:1200px;height:128px;background:var(--white)}
.site-footer .brand{left:120px;top:36px}
.footer-nav{position:absolute;left:440px;top:38px;display:flex;gap:26px;font-size:12px;font-weight:700;color:var(--navy)}
.footer-nav span.sep{color:#9aa3ad;font-weight:400}
.copyright{position:absolute;left:520px;top:70px;font-size:11px;color:var(--text)}
.footer-swoosh{position:absolute;right:0;top:0}
</style>
</head>
<body>

<header class="site-header">
  <div class="brand"><div class="brand-mark"></div><span class="brand-name">Lantern Advisory</span></div>
  <svg class="header-swoosh" width="870" height="88" viewBox="0 0 870 88">
    <path d="M0 88 C60 40 90 10 170 0 L870 0 L870 72 L150 72 C90 72 60 80 0 88Z" fill="#1d87d4"/>
    <path d="M0 88 C70 60 110 78 180 78 L870 78 L870 72 L150 72 C90 72 60 80 0 88Z" fill="#0a4d8c"/>
  </svg>
  <nav class="main-nav">
    <a>COMPANY</a><a>SERVICES</a><a>SOLUTIONS</a><a>RESOURCES</a><a>CAREER</a><a>CONTACT US</a>
  </nav>
</header>

<section class="hero">
  <div class="hero-photo" role="img" aria-label="Blue technology scene with interlocking gears"></div>
  <div class="hero-content">
    <h1 class="hero-title">LANTERN ADVISORY</h1>
    <p class="hero-text">We combine proven methods with fresh ideas to help organisations modernise their technology, reduce risk and grow with confidence.</p>
    <span class="btn">LEARN MORE</span>
  </div>
  <div class="dots" style="top:470px"><span class="on"></span><span></span><span></span></div>
</section>

<section class="welcome">
  <h2 class="section-title">Welcome to Lantern Advisory</h2>
  <p>Lantern Advisory is a dynamic, fast-paced consulting firm with a steady record of growth. Our technical experts and business analysts work closely with clients across many industries, shaping solutions that fit each goal. We partner with leading platforms to deliver dependable results, on time and on budget.</p>
  <span class="btn btn-outline">LEARN MORE</span>
</section>

<section class="services">
  <h2 class="section-title">Our Services</h2>
  <div class="service-row">
    <div class="service-card">
      <div class="service-head">
        <div class="service-icon"><svg width="20" height="20" viewBox="0 0 20 20"><rect x="3" y="10" width="3" height="7" fill="#1d87d4"/><rect x="8.5" y="6" width="3" height="11" fill="#1d87d4"/><rect x="14" y="3" width="3" height="14" fill="#1d87d4"/></svg></div>
        <span class="service-name">Business</span>
      </div>
      <p>Clear planning and expert delivery for every stage of your project, from first idea to final launch and support.</p>
    </div>
    <div class="service-card">
      <div class="service-head">
        <div class="service-icon"><svg width="20" height="20" viewBox="0 0 20 20"><rect x="2" y="3" width="16" height="11" rx="1" fill="none" stroke="#1d87d4" stroke-width="2"/><rect x="7" y="15" width="6" height="2" fill="#1d87d4"/></svg></div>
        <span class="service-name">Technology</span>
      </div>
      <p>Modern systems chosen with care, built to last and tuned to the way your teams already like to work each day.</p>
    </div>
    <div class="service-card">
      <div class="service-head">
        <div class="service-icon"><svg width="20" height="20" viewBox="0 0 20 20"><rect x="3" y="3" width="6" height="6" fill="#1d87d4"/><rect x="11" y="3" width="6" height="6" fill="#1d87d4"/><rect x="3" y="11" width="6" height="6" fill="#1d87d4"/><rect x="11" y="11" width="6" height="6" fill="#1d87d4"/></svg></div>
        <span class="service-name">Application</span>
      </div>
      <p>Custom software designed around your users, tested thoroughly and kept secure through updates and steady support.</p>
    </div>
  </div>
  <div class="dots"><span class="on"></span><span></span><span></span><span></span><span></span></div>
</section>

<section class="feature it">
  <div class="feature-photo" role="img" aria-label="Team working together at laptops in a bright office"></div>
  <div class="feature-body">
    <h2 class="feature-title">IT Consulting</h2>
    <p>Information technology should improve business results. Our team helps companies make sense of data, choose the right systems and plan upgrades that keep daily work running smoothly.</p>
    <p>We draw on broad experience across industries to give clients a clear path forward, balancing cost, speed and quality at every step.</p>
  </div>
</section>

<section class="feature staff">
  <div class="feature-body">
    <h2 class="feature-title">Staff Augmentation</h2>
    <p>Our staffing service gives you skilled professionals when you need them most. We match each role with people who understand your tools, your pace and your goals, so new team members add value from the first day.</p>
  </div>
  <div class="feature-photo" role="img" aria-label="Silhouettes of business people walking past tall glass buildings"></div>
</section>

<section class="feature offshore">
  <div class="feature-photo" role="img" aria-label="Consultant at a desk reviewing plans"></div>
  <div class="feature-body">
    <h2 class="feature-title">Offshore</h2>
    <p>Our offshore delivery model pairs local project leadership with a trusted remote team, giving you round-the-clock progress, lower costs and the flexibility to scale quickly.</p>
  </div>
</section>

<footer class="site-footer">
  <div class="brand"><div class="brand-mark"></div><span class="brand-name">Lantern Advisory</span></div>
  <div class="footer-nav">
    <span>COMPANY</span><span class="sep">|</span><span>SERVICES</span><span class="sep">|</span><span>SOLUTIONS</span><span class="sep">|</span><span>RESOURCES</span><span class="sep">|</span><span>CAREER</span><span class="sep">|</span><span>CONTACT US</span>
  </div>
  <p class="copyright">© 2024 LANTERN ADVISORY, ALL RIGHTS RESERVED</p>
  <svg class="footer-swoosh" width="120" height="128" viewBox="0 0 120 128">
    <path d="M120 0 L120 128 L40 128 C80 100 100 50 120 0Z" fill="#1d87d4"/>
    <path d="M120 40 L120 128 L80 128 C100 110 112 80 120 40Z" fill="#0a4d8c"/>
  </svg>
</footer>

</body>
</html>
```